Tree company needs modern website design

We need a website design for a tree company, here are some websites they like:

http://harborvantage.com/company/ - we like the big image filling most of the page. Also the top half of the page looks good with the logo along top and good task bar also (we don’t like the spiel on left hand side covering up the picture + too many words!) If we could have our logo at lop like this along with our slogan which is 'Proud Standing Boughs that Thrive Strong'

http://www.wilmotgrovenurseries.co.nz/ - we like the bottom half of this with the clean lines and welcome to part down bottom rather than the spiel to the left as on above site. Also like the moving leaves, any chance we could have birds such as a fantail, Tui and Bellbirds flying across the page and also some birdsong playing?

This is their existing website, that needs an updated design: http://tallpineshade.co.nz/

Industry/Entity Type

It Company

Font styles to use
Serif
Sans Serif

Requirements
Must have
• "Website by Pagecraft Studio Co" located in bottom right hand side
Use images provided as background or banner images
Should not have
• Social Media icons

```html
<!DOCTYPE html>
<html lang="en">
<head>
<meta charset="utf-8">
<title>Tall Pine Shade</title>
<link href="https://fonts.googleapis.com/css2?family=Carlito:wght@400;700&display=swap" rel="stylesheet">
<style>
  :root {
    --green: #23902a;
    --lime: #a8c20c;
    --lime-bright: #c6f023;
    --yellow: #ffd800;
    --yellow-band: #fff200;
    --card-green: #d8f58e;
    --ink: #3d4a1a;
    --muted: #4f5b2c;
    --white: #ffffff;
  }
  * { box-sizing: border-box; margin: 0; padding: 0; }
  html, body { width: 1186px; height: 1200px; overflow: hidden; }
  body { font-family: "Carlito", sans-serif; background: var(--green); position: relative; }

  .site-header { position: absolute; left: 0; top: 0; width: 1186px; height: 127px; background: var(--green); }
  .header-rule { position: absolute; left: 0; top: 127px; width: 1186px; height: 6px; background: var(--lime); }
  .brand { position: absolute; left: 190px; top: 62px; display: flex; align-items: center; gap: 10px; }
  .brand-dot { width: 22px; height: 22px; border-radius: 50%; background: var(--yellow); }
  .brand-name { font-size: 36px; font-weight: 700; color: var(--yellow); line-height: 1; letter-spacing: 1px; }
  .main-nav { position: absolute; top: 74px; left: 0; width: 100%; }
  .main-nav a { position: absolute; font-size: 12px; font-weight: 700; color: var(--white); text-decoration: none; }
  .main-nav a.is-active { color: var(--yellow); }
  .nav-marker { position: absolute; left: 571px; top: 124px; width: 34px; height: 3px; background: var(--yellow); }

  .hero { position: absolute; left: 0; top: 133px; width: 1186px; height: 888px;
    background: linear-gradient(180deg, #3e6fb0 0%, #7da2cf 25%, #d9e2ec 55%, #5e6a52 72%, #7a6a43 80%, #a8a49a 90%, #8e8b83 100%); }

  .projects-title { position: absolute; left: 302px; top: 172px; font-size: 15px; font-weight: 700; color: var(--yellow); }
  .projects-bar { position: absolute; left: 396px; top: 174px; width: 525px; height: 15px; background: var(--yellow); }
  .project-card { position: absolute; top: 202px; width: 186px; height: 171px; background: var(--card-green);
    border: 1px solid #f2f2f2; box-shadow: 0 2px 4px rgba(0,0,0,.3); text-align: center; }
  .project-card .thumb { position: absolute; left: 5px; top: 5px; width: 175px; height: 111px; border: 1px solid #fff; }
  .project-card h3 { position: absolute; top: 126px; width: 100%; font-size: 12.5px; font-weight: 700; color: var(--ink); }
  .project-card p { position: absolute; top: 143px; width: 100%; font-size: 10px; color: var(--muted); word-spacing: 2px; }
  .zoom { position: absolute; left: 66px; top: 29px; width: 55px; height: 55px; border-radius: 50%; background: rgba(30,30,30,.7); }

  .caption-panel { position: absolute; left: 407px; top: 517px; width: 410px; height: 108px; background: rgba(255,255,255,.45); }
  .caption-band { position: absolute; left: 386px; top: 528px; width: 451px; height: 31px; background: var(--yellow-band); }
  .caption-title { position: absolute; left: 419px; top: 532px; font-size: 18px; font-weight: 700; color: var(--ink); }
  .caption-text { position: absolute; left: 419px; top: 574px; width: 392px; font-size: 11.5px; line-height: 18px; color: #333; text-align: justify; }

  .slide-arrow { position: absolute; top: 537px; width: 30px; height: 42px; display: flex; align-items: center; justify-content: center; }
  .slide-arrow.prev { left: 0; background: #555a5c; }
  .slide-arrow.next { left: 1155px; background: var(--lime-bright); }

  .footer-rule { position: absolute; left: 0; top: 1021px; width: 1186px; height: 12px; background: var(--green); border-top: 4px solid var(--green); }
  .footer-rule::after { content: ""; position: absolute; left: 0; top: 4px; width: 100%; height: 8px; background: var(--lime); }
  .site-footer { position: absolute; left: 0; top: 1033px; width: 1186px; height: 129px; background: var(--green); text-align: center; }
  .footer-trees { position: absolute; left: 0; top: 65px; width: 100%; height: 64px; background: linear-gradient(180deg, rgba(40,160,40,0) 0%, #2aa234 40%, #2aa234 100%); }
  .footer-name { position: relative; top: 23px; font-size: 19px; color: var(--yellow); }
  .footer-contact { position: relative; top: 23px; font-size: 11px; line-height: 16px; color: var(--white); }
  .bottom-bar { position: absolute; left: 0; top: 1162px; width: 1186px; height: 38px; background: #9cbb10; font-size: 11px; color: var(--white); }
  .bottom-bar .copyright { position: absolute; left: 189px; top: 12px; }
  .bottom-bar .credit { position: absolute; right: 201px; top: 12px; }
</style>
</head>
<body>
  <header class="site-header">
    <div class="brand"><span class="brand-dot"></span><span class="brand-name">TALL PINE SHADE</span></div>
    <nav class="main-nav">
      <a class="is-active" style="left:573px">Home</a>
      <a style="left:626px">Pages</a>
      <a style="left:679px">Portfolio</a>
      <a style="left:746px">Shortcodes</a>
      <a style="left:828px">Features</a>
      <a style="left:894px">Blog</a>
      <a style="left:940px">Contact</a>
    </nav>
    <div class="nav-marker"></div>
  </header>
  <div class="header-rule"></div>

  <main>
    <div class="hero" role="img" aria-label="Landscape photo of a gravel road winding past young trees under a cloudy blue sky with mountains"></div>

    <div class="projects-title">Latest Projets</div>
    <div class="projects-bar"></div>

    <article class="project-card" style="left:300px">
      <div class="thumb" role="img" aria-label="Photo of a house in front of rocky mountains" style="background:linear-gradient(180deg,#4a78c0 0%,#8a8270 45%,#4f7a3a 100%)">
        <div class="zoom"><svg width="55" height="55" viewBox="0 0 55 55"><circle cx="26" cy="26" r="5" fill="none" stroke="#fff" stroke-width="2"/><line x1="30" y1="30" x2="34" y2="34" stroke="#fff" stroke-width="2.5"/></svg></div>
      </div>
      <h3>Tall Pine Shade</h3>
      <p>Text Text Text Text Text Text</p>
    </article>
    <article class="project-card" style="left:517px">
      <div class="thumb" role="img" aria-label="Photo of a modern stone house with planted garden" style="background:linear-gradient(180deg,#b8c6d0 0%,#6a5a48 40%,#5a6848 100%)"></div>
      <h3>Tall Pine Shade</h3>
      <p>Text Text Text Text Text Text</p>
    </article>
    <article class="project-card" style="left:734px">
      <div class="thumb" role="img" aria-label="Photo of a modern building with a landscaped roadside" style="background:linear-gradient(180deg,#4d86cc 0%,#c8d4de 40%,#5c6a50 70%,#9a9a98 100%)"></div>
      <h3>Tall Pine Shade</h3>
      <p>Text Text Text Text Text Text</p>
    </article>

    <div class="caption-panel"></div>
    <div class="caption-band"></div>
    <h2 class="caption-title">Carpinus betulus - Hornbeam</h2>
    <p class="caption-text">Hornbeam. A hardy deciduous smaller tree or shrub with lush green spring/summer foliage, excellent for hedging.</p>

    <div class="slide-arrow prev"><svg width="12" height="16" viewBox="0 0 12 16"><path d="M9 2 L3 8 L9 14" fill="none" stroke="#fff" stroke-width="2.5"/></svg></div>
    <div class="slide-arrow next"><svg width="12" height="16" viewBox="0 0 12 16"><path d="M3 2 L9 8 L3 14" fill="none" stroke="#fff" stroke-width="2.5"/></svg></div>
  </main>

  <div class="footer-rule"></div>
  <footer class="site-footer">
    <div class="footer-trees" role="img" aria-label="Row of tree silhouettes"></div>
    <div class="footer-name">Tall Pine Shade</div>
    <div class="footer-contact">
      58 Kestrel Lane, Fernvale 9840<br>
      Toll free: 0508 400 123<br>
      Ph: (03) 555 0142, Fax: (03) 555 0187<br>
      Email: sales@tallpineshade.co.nz
    </div>
  </footer>
  <div class="bottom-bar">
    <span class="copyright">Copyright @ 2014</span>
    <span class="credit">Website by Pagecraft Studio Co</span>
  </div>
</body>
</html>
```